The Holloway Lodge (Ebook cover design)

Trying to find the perfect ebook cover design for my novel. Its a thriller/horror novel. I like very subtle yet chilling covers. I'll attach some book covers that I love for inspiration.
My book takes place mostly in a large cabin in the middle of the woods during the summer at night. Its also a survival type horror if that helps. I would like the color red or black to be the backdrop. Its for a brindle edition novel, and I'm using word. I would like my name on the top as the author (Mirela Dunstrove) and the title of the novel "The Holloway Lodge" in the middle or bottom, whatever looks best. I'm just looking for something subtle but not too over the top.
Another idea I have is a shovel stuck in the dirt above a open grave with a hand coming out.
Thanks in advance, I appreciate all submissions!
Other font styles liked:
- Copperplate Gothic Light
Requirements
Must have
- Author name and title of book
Nice to have
- Red or black background/ eerie dark setting/ author name and book title in black or red
Should not have
- Bright colors

```html
<!DOCTYPE html>
<html lang="en">
<head>
<meta charset="utf-8">
<title>The Holloway Lodge — Ebook Cover</title>
<link rel="stylesheet" href="https://fonts.googleapis.com/css2?family=Bebas+Neue&family=IM+Fell+English+SC&display=swap">
<style>
  :root {
    --stage: #4a4a4a;
    --ink: #000000;
    --blood: #c8101a;
    --glow: #ec0a10;
    --crimson: #b30207;
    --ember: #5e0204;
    --soot: #1a0001;
    --bone: #f4f1ec;
  }
  html, body {
    margin: 0;
    width: 1200px;
    height: 897px;
    overflow: hidden;
    background: var(--stage);
  }
  .cover {
    position: absolute;
    left: 320px;
    top: 28px;
    width: 560px;
    height: 840px;
    background: var(--ink);
    overflow: hidden;
  }
  .cover-art {
    position: absolute;
    left: 0;
    top: 0;
    width: 560px;
    height: 680px;
    background:
      linear-gradient(to bottom, rgba(0,0,0,0) 0%, rgba(0,0,0,0) 78%, rgba(0,0,0,0.9) 93%, var(--ink) 100%),
      radial-gradient(ellipse 46% 26% at 50% 67%, rgba(10,0,0,0.92) 0%, rgba(25,0,1,0.85) 55%, rgba(0,0,0,0) 100%),
      radial-gradient(ellipse 55% 14% at 50% 50%, rgba(30,0,1,0.75) 0%, rgba(0,0,0,0) 100%),
      linear-gradient(to right, rgba(0,0,0,0.85) 0%, rgba(0,0,0,0.2) 12%, rgba(0,0,0,0) 22%, rgba(0,0,0,0) 80%, rgba(0,0,0,0.3) 90%, rgba(0,0,0,0.9) 100%),
      linear-gradient(to bottom, rgba(0,0,0,0.55) 0%, rgba(0,0,0,0) 14%),
      radial-gradient(ellipse 70% 55% at 42% 34%, var(--glow) 0%, var(--crimson) 45%, var(--ember) 78%, var(--soot) 100%);
  }
  .author {
    position: absolute;
    left: 0;
    top: 74px;
    width: 560px;
    margin: 0;
    text-align: center;
    font-family: "IM Fell English SC", Georgia, serif;
    font-weight: 400;
    font-size: 36px;
    line-height: 44px;
    letter-spacing: 0.15em;
    text-indent: 0.15em;
    color: var(--bone);
  }
  .tagline {
    position: absolute;
    left: 0;
    top: 628px;
    width: 560px;
    margin: 0;
    text-align: center;
    font-family: "IM Fell English SC", Georgia, serif;
    font-size: 14px;
    line-height: 18px;
    letter-spacing: 0.5em;
    text-indent: 0.5em;
    color: var(--bone);
  }
  .title {
    position: absolute;
    left: 0;
    top: 660px;
    width: 560px;
    height: 160px;
  }
  .title-small {
    font-family: "IM Fell English SC", Georgia, serif;
    fill: var(--bone);
  }
  .title-main {
    font-family: "Bebas Neue", Impact, sans-serif;
    fill: var(--blood);
  }
</style>
</head>
<body>
  <main class="cover">
    <div class="cover-art" role="img" aria-label="Dark shingled cabin silhouette with a lit window, standing in a misty forest washed in deep red"></div>
    <p class="author">MIRELA DUNSTROVE</p>
    <p class="tagline">A NOVEL</p>
    <svg class="title" viewBox="0 0 560 160" aria-label="The Holloway Lodge" role="img">
      <defs>
        <filter id="distressed-ink" x="0" y="0" width="100%" height="100%">
          <feTurbulence type="fractalNoise" baseFrequency="0.32" numOctaves="3" seed="7" result="noise"/>
          <feColorMatrix in="noise" type="matrix" values="0 0 0 0 0  0 0 0 0 0  0 0 0 0 0  0 0 0 -3 2.35" result="wear"/>
          <feComposite in="SourceGraphic" in2="wear" operator="in"/>
        </filter>
      </defs>
      <text class="title-small" font-size="24" letter-spacing="2" transform="translate(120 44) rotate(-90)" text-anchor="middle">THE</text>
      <text class="title-main" filter="url(#distressed-ink)" x="124" y="126" font-size="158" textLength="332" lengthAdjust="spacingAndGlyphs">HOLLOWAY</text>
      <text class="title-small" x="452" y="146" font-size="17" letter-spacing="10" text-anchor="end">LODGE</text>
    </svg>
  </main>
</body>
</html>
```